Professional Home Buyer business card needed

I need a pretty straight forward business card designed. We help people that NEED to sell their homes solve problems. We perform all types of Real Estate transactions including flip, wholesale, investment, rental property and multi family. The card will mainly be used to give to prospective Sellers but will also be given to Real Estate Investors as well. It should professional and very easy to read, most clients are older people.

Target Market(s)

Distressed home sellers as well as Real Estate investors

Industry/Entity Type

Real Estate

Contact Information for Business Card

should be a professional layout

Colors
ec1f27
ffffff
000000

Requirements
Must have
• Large logo on back and smaller one on front. should utilize Red, white, and black.
• I am thinking of using a soft touch coating on the card so keep that in mind.
• Contact info should be very easy to read, think older clients.
Nice to have
• I would like to see a design with rounded corners on the card
Should not have
• pictures of homes or other home graphics.

```html
<!DOCTYPE html>
<html lang="en">
<head>
<meta charset="utf-8">
<title>Keystone Home Buyers – Business Card</title>
<link rel="stylesheet" href="https://fonts.googleapis.com/css2?family=Montserrat:wght@400;600;700&display=swap">
<style>
  :root {
    --brand-red: #ec1f27;
    --ink: #000000;
    --charcoal: #343739;
    --paper: #ffffff;
    --muted: #555a5e;
    --backdrop: #8a8c8e;
  }
  * { box-sizing: border-box; margin: 0; padding: 0; }
  html, body { width: 1200px; height: 900px; overflow: hidden; }
  body {
    background: var(--backdrop);
    font-family: "Montserrat", sans-serif;
    position: relative;
  }
  .card {
    position: absolute;
    left: 280px;
    width: 640px;
    height: 366px;
    border-radius: 18px;
    overflow: hidden;
    box-shadow: 0 10px 30px rgba(0,0,0,.3);
  }
  .card-back { top: 60px; background: var(--charcoal); }
  .card-front { top: 470px; background: var(--paper); }

  .wordmark {
    display: flex;
    align-items: center;
    gap: 14px;
    font-weight: 700;
    text-transform: uppercase;
    letter-spacing: .06em;
    line-height: 1;
    white-space: nowrap;
  }
  .wordmark-square { flex: none; background: var(--brand-red); }

  .card-back .wordmark {
    position: absolute; inset: 0;
    justify-content: center;
    color: var(--paper);
    font-size: 30px;
  }
  .card-back .wordmark-square { width: 30px; height: 30px; }

  .card-front .wordmark {
    position: absolute; right: 36px; top: 74px;
    color: var(--ink);
    font-size: 19px;
    gap: 10px;
  }
  .card-front .wordmark-square { width: 19px; height: 19px; }

  .contact { position: absolute; left: 40px; top: 64px; }
  .contact-name {
    color: var(--brand-red);
    font-size: 26px;
    font-weight: 400;
    letter-spacing: .02em;
  }
  .contact-title { color: var(--muted); font-size: 16px; margin-top: 4px; }
  .contact-list { list-style: none; margin-top: 26px; }
  .contact-item {
    display: flex; align-items: center; gap: 14px;
    font-size: 17px; color: var(--ink);
    margin-bottom: 10px;
  }
  .contact-icon { width: 16px; height: 16px; flex: none; }

  .address-band {
    position: absolute; left: 0; right: 0; bottom: 0;
    height: 78px;
    background: var(--charcoal);
    border-top: 4px solid var(--paper);
    box-shadow: 0 -3px 0 var(--brand-red);
    display: flex; align-items: center; justify-content: center;
    color: var(--paper);
    font-size: 18px;
    letter-spacing: .04em;
  }
</style>
</head>
<body>
  <section class="card card-back" aria-label="Card back">
    <div class="wordmark">
      <span class="wordmark-square"></span>
      <span class="wordmark-name">Keystone Home Buyers</span>
    </div>
  </section>

  <section class="card card-front" aria-label="Card front">
    <div class="contact">
      <h1 class="contact-name">JOHN DOE</h1>
      <p class="contact-title">Director</p>
      <ul class="contact-list">
        <li class="contact-item">
          <svg class="contact-icon" viewBox="0 0 16 16" aria-hidden="true"><path d="M3 1l3 3-1.5 2a9 9 0 0 0 5.5 5.5L12 10l3 3-2 2C7 15 1 9 1 3z" fill="var(--brand-red)"/></svg>
          <span>555-218-0147</span>
        </li>
        <li class="contact-item">
          <svg class="contact-icon" viewBox="0 0 16 16" aria-hidden="true"><rect x="1" y="3" width="14" height="10" fill="var(--brand-red)"/><path d="M1 3l7 6 7-6" stroke="#fff" stroke-width="1.4" fill="none"/></svg>
          <span>john.doe@keystone</span>
        </li>
        <li class="contact-item">
          <svg class="contact-icon" viewBox="0 0 16 16" aria-hidden="true"><circle cx="8" cy="8" r="6.5" stroke="var(--brand-red)" stroke-width="1.4" fill="none"/><ellipse cx="8" cy="8" rx="2.8" ry="6.5" stroke="var(--brand-red)" stroke-width="1.2" fill="none"/><path d="M1.5 8h13" stroke="var(--brand-red)" stroke-width="1.2"/></svg>
          <span>www.keystone</span>
        </li>
      </ul>
    </div>

    <div class="wordmark">
      <span class="wordmark-square"></span>
      <span class="wordmark-name">Keystone Home Buyers</span>
    </div>

    <footer class="address-band">48 Cedar Lane, Brookfield, AB, T2X 4K8</footer>
  </section>
</body>
</html>
```